Copperfield Hide Renewal Product Label

We need a design for a label to be used on bottles of leather cleaner and conditioner products that will be used in curated kits. We would like it to incorporate our business logo as well as have an area that we can fill in later with the appropriate product name as needed. We would like to see designs that use shades of brown, but we are open to other colors often seen in leather. I am including the Copperfield Hide business Logo below, however again we would prefer to have the label in various shades of browns, rather than the red and grey, more like the mock-up that I am also attaching.

*** I am attaching examples of the types of bottles that will be used. They vary in size from 8 oz to 16 oz. if you are designing a label for a spray bottle they are from 16-32 oz. ***

```html
<!DOCTYPE html>
<html lang="en">
<head>
<meta charset="utf-8">
<title>Copperfield Hide Renewal – Leather Cleaner Label</title>
<link href="https://fonts.googleapis.com/css2?family=Cinzel:wght@400;500&family=Barlow+Condensed:ital,wght@0,500;1,500&display=swap" rel="stylesheet">
<style>
  :root {
    --backdrop: #b9c2cc;
    --gold-dark: #6a4708;
    --gold-mid: #9a6f12;
    --gold-light: #c99a2e;
    --maroon-light: #5e1b1d;
    --maroon-dark: #3a0e11;
    --badge-tan: #a8642c;
    --badge-dark: #7a4219;
    --ink-light: #ffffff;
    --ink-dark: #3a0e11;
  }
  html, body {
    margin: 0;
    width: 1200px;
    height: 833px;
    overflow: hidden;
    background: var(--backdrop);
  }
  .label {
    position: absolute;
    left: 370px;
    top: 52px;
    width: 460px;
    height: 730px;
  }
  .label svg { display: block; }
  .brand-name {
    font-family: "Barlow Condensed", sans-serif;
    font-weight: 500;
    font-size: 16px;
    fill: var(--ink-dark);
  }
  .title-main {
    font-family: "Cinzel", serif;
    font-weight: 500;
    font-size: 64px;
    fill: var(--ink-light);
  }
  .title-sub {
    font-family: "Cinzel", serif;
    font-weight: 500;
    font-size: 34px;
    letter-spacing: 9px;
    fill: var(--ink-dark);
  }
  .feature {
    font-family: "Barlow Condensed", sans-serif;
    font-style: italic;
    font-weight: 500;
    font-size: 20px;
    fill: var(--ink-light);
  }
  .volume {
    font-family: "Barlow Condensed", sans-serif;
    font-weight: 500;
    font-size: 22px;
    fill: var(--ink-light);
  }
  .tagline {
    font-family: "Barlow Condensed", sans-serif;
    font-style: italic;
    font-weight: 500;
    font-size: 22px;
    fill: var(--ink-light);
  }
</style>
</head>
<body>
<div class="label">
  <svg width="460" height="730" viewBox="0 0 460 730" xmlns="http://www.w3.org/2000/svg">
    <defs>
      <linearGradient id="gold-fill" x1="0" y1="0" x2="1" y2="1">
        <stop offset="0" stop-color="var(--gold-dark)"/>
        <stop offset="0.5" stop-color="var(--gold-mid)"/>
        <stop offset="1" stop-color="var(--gold-dark)"/>
      </linearGradient>
      <radialGradient id="maroon-fill" cx="0.5" cy="0.45" r="0.7">
        <stop offset="0" stop-color="var(--maroon-light)"/>
        <stop offset="1" stop-color="var(--maroon-dark)"/>
      </radialGradient>
      <linearGradient id="badge-fill" x1="0" y1="0" x2="0" y2="1">
        <stop offset="0" stop-color="var(--badge-tan)"/>
        <stop offset="1" stop-color="var(--badge-dark)"/>
      </linearGradient>
    </defs>

    <path class="label-base" d="M0 14 Q0 0 14 0 H446 Q460 0 460 14 V730 H0 Z" fill="url(#gold-fill)" role="img" aria-label="Gold band with faint tooled leather flourishes"/>

    <path class="centre-panel" d="M0 152 Q230 125 460 152 V600 Q230 625 0 600 Z" fill="url(#maroon-fill)"/>

    <path d="M0 146 Q230 119 460 146" fill="none" stroke="var(--gold-light)" stroke-width="3"/>
    <path d="M0 160 Q230 133 460 160" fill="none" stroke="var(--gold-light)" stroke-width="1.2" stroke-dasharray="3 3"/>
    <path d="M0 592 Q230 617 460 592" fill="none" stroke="var(--gold-light)" stroke-width="1.2" stroke-dasharray="3 3"/>
    <path d="M0 606 Q230 631 460 606" fill="none" stroke="var(--gold-light)" stroke-width="3"/>

    <!-- brand badge -->
    <rect class="brand-badge" x="120" y="72" width="220" height="118" rx="26" fill="url(#badge-fill)" stroke="var(--badge-dark)" stroke-width="2"/>
    <rect x="130" y="82" width="200" height="98" rx="20" fill="none" stroke="#e0b57a" stroke-width="1.2" stroke-dasharray="4 3"/>
    <rect x="142" y="125" width="12" height="12" fill="var(--ink-dark)"/>
    <text class="brand-name" x="160" y="137" textLength="158" lengthAdjust="spacingAndGlyphs">Copperfield Hide Renewal</text>

    <!-- product title -->
    <text class="title-main" x="230" y="350" text-anchor="middle">LEATHER</text>
    <path class="ribbon-tail" d="M8 366 H30 V398 H8 L16 382 Z" fill="var(--ink-light)"/>
    <path class="ribbon-tail" d="M452 366 H430 V398 H452 L444 382 Z" fill="var(--ink-light)"/>
    <rect class="ribbon" x="26" y="358" width="408" height="48" fill="var(--ink-light)"/>
    <rect x="30" y="362" width="400" height="40" fill="none" stroke="var(--ink-dark)" stroke-width="1.5"/>
    <text class="title-sub" x="234" y="395" text-anchor="middle">CLEANER</text>
    <line x1="50" y1="418" x2="410" y2="418" stroke="var(--ink-light)" stroke-width="1.5"/>

    <!-- features -->
    <circle cx="30" cy="485" r="4" fill="none" stroke="var(--ink-light)" stroke-width="2"/>
    <text class="feature" x="42" y="492">Thick, rich lotion</text>
    <circle cx="30" cy="511" r="4" fill="none" stroke="var(--ink-light)" stroke-width="2"/>
    <text class="feature" x="42" y="518">Leaves a non-poly, natural, soft, supple finish</text>
    <circle cx="30" cy="537" r="4" fill="none" stroke="var(--ink-light)" stroke-width="2"/>
    <text class="feature" x="42" y="544">Pleasant fragrance</text>

    <!-- volume and claim -->
    <text class="volume" x="230" y="676" text-anchor="middle">16 US FL. OZ 473 ML</text>
    <text class="tagline" x="230" y="702" text-anchor="middle">pH Balanced Superior Cleaner</text>
  </svg>
</div>
</body>
</html>
```